Digital Marketing Consultant Needs a Business Card Design

I need a business card to brand myself - I'm a digital marketing consultant, and I do web design, SEO, lead generation, social media, etc. I'm overhauling my website (CorinneHalvorsk.com) and just had a snazzy new logo made.

I like the combo of yellow & gray - I find it eye-catching, upbeat and techie. The exact colors of yellow and gray that I like are #F6BF27 and #6D6D6D. But I'm open to suggestions and other color combinations!

I plan on printing the card using some high-end printing techniques that will ensure the card stands out - either really thick cards with colored edges, or spot UV. Not sure which yet, so if you want to incorporate that into your design, that'd be great!

I'm looking for a clean and modern design, but something that will really stand out when paired with 'fancy' printing.

Target Market(s)

Small and medium-sized business owners.

Industry/Entity Type

Printing

Contact Information for Business Card

Corinne Halvorsk
Digital Marketing
Call or Text: 850-555-0927
Corinne@CorinneHalvorsk.com
www.CorinneHalvorsk.com
@QPZ47 on Twitter

Font styles to use
Serif
Sans Serif

Requirements
Must have
• My logo, my contact information, and my "company colors" - #F6BF27 and #6D6D6D.
Nice to have
• If there's room to mention all the things that I do:
• Social Media, Web Design, SEO, Lead Generation, Conversion Funnels, PPC
• (don't add if it makes the card cluttered)

```html
<!DOCTYPE html>
<html lang="en">
<head>
<meta charset="utf-8">
<title>Corinne Halvorsk – Business Card</title>
<link href="https://fonts.googleapis.com/css2?family=Marcellus&family=Montserrat:wght@400;600;700&display=swap" rel="stylesheet">
<style>
  :root {
    --backdrop: #2a2a2a;
    --card-black: #0b0b0b;
    --brand-yellow: #F6BF27;
    --brand-gray: #6D6D6D;
    --soft-gray: #9a9a9a;
    --white: #ffffff;
    --serif: "Marcellus", Georgia, serif;
    --sans: "Montserrat", Arial, sans-serif;
  }
  * { margin: 0; padding: 0; box-sizing: border-box; }
  html, body { width: 1200px; height: 802px; overflow: hidden; }
  body { background: var(--backdrop); position: relative; font-family: var(--sans); }

  .card {
    position: absolute;
    top: 252px;
    width: 520px;
    height: 297px;
    border-radius: 22px;
    background: var(--card-black);
    overflow: hidden;
    box-shadow: 0 10px 30px rgba(0,0,0,.5);
  }

  /* Services side */
  .card--services { left: 60px; }
  .service {
    position: absolute;
    font-family: var(--sans);
    font-weight: 600;
    font-size: 13px;
    line-height: 1.2;
    text-align: center;
    color: var(--brand-gray);
  }
  .service--accent { color: var(--brand-yellow); }
  .services__name {
    position: absolute;
    left: 0; right: 0; top: 132px;
    text-align: center;
    font-family: var(--serif);
    font-size: 30px;
    letter-spacing: 2px;
    color: var(--soft-gray);
  }
  .services__rule {
    position: absolute;
    left: 150px; width: 220px; top: 176px;
    height: 1px; background: var(--brand-gray);
  }

  /* Contact side */
  .card--contact { left: 620px; }
  .contact__brand {
    position: absolute;
    left: 0; top: 0; width: 250px; height: 100%;
    background: var(--card-black);
  }
  .brand__square {
    position: absolute;
    left: 100px; top: 92px;
    width: 44px; height: 44px;
    border: 2px solid var(--soft-gray);
  }
  .brand__name {
    position: absolute;
    left: 0; right: 0; top: 154px;
    text-align: center;
    font-family: var(--serif);
    font-size: 20px;
    letter-spacing: 1px;
    color: var(--soft-gray);
  }
  .brand__rule {
    position: absolute;
    left: 30px; width: 170px; top: 186px;
    height: 1px; background: var(--brand-gray);
  }

  .contact__details {
    position: absolute;
    left: 250px; top: 0; right: 0; height: 100%;
    background: var(--brand-yellow);
    color: var(--white);
  }
  .details__name {
    position: absolute; right: 34px; top: 20px;
    font-size: 19px; font-weight: 400;
  }
  .details__title {
    position: absolute; right: 34px; top: 44px;
    font-size: 12px;
  }
  .details__rule {
    position: absolute; height: 1px; background: #1a1a1a;
  }
  .details__rule--top { left: 40px; right: 34px; top: 62px; }
  .details__rule--mid { left: 10px; right: 70px; top: 168px; }
  .details__rule--low { left: 10px; right: 0; top: 182px; }
  .details__line {
    position: absolute; right: 34px;
    font-size: 12.5px; text-align: right;
  }
  .details__icon { position: absolute; right: 12px; }
  .details__heading {
    position: absolute; left: 10px; top: 150px;
    font-size: 13px;
  }
  .company-row {
    position: absolute; left: 14px;
    display: flex; align-items: flex-start; gap: 10px;
    font-size: 13.5px; line-height: 1.25;
  }
  .company-row svg { flex: none; margin-top: 2px; }
</style>
</head>
<body>

  <section class="card card--services" aria-label="Card back with services">
    <span class="service service--accent" style="left:245px; top:40px;">Web<br>Design</span>
    <span class="service" style="left:400px; top:28px;">SEO</span>
    <span class="service service--accent" style="left:420px; top:92px;">PPC</span>
    <span class="service" style="left:70px; top:92px;">Social<br>Media</span>
    <span class="service" style="left:320px; top:206px;">Conversion<br>Funnels</span>
    <span class="service service--accent" style="left:140px; top:226px;">Lead<br>Generation</span>
    <div class="services__name">CORINNE HALVORSK</div>
    <div class="services__rule"></div>
  </section>

  <section class="card card--contact" aria-label="Card front with contact details">
    <div class="contact__brand">
      <div class="brand__square"></div>
      <div class="brand__name">CORINNE HALVORSK</div>
      <div class="brand__rule"></div>
    </div>

    <div class="contact__details">
      <div class="details__name">Corinne Halvorsk</div>
      <div class="details__title">Managing Director.</div>
      <div class="details__rule details__rule--top"></div>

      <div class="details__line" style="top:72px;">850-555-0927</div>
      <svg class="details__icon" style="top:72px;" width="10" height="15" viewBox="0 0 10 15" aria-hidden="true">
        <rect x="1" y="1" width="8" height="13" rx="1.5" fill="none" stroke="#fff" stroke-width="1.4"/>
        <circle cx="5" cy="11.5" r="0.9" fill="#fff"/>
      </svg>

      <div class="details__line" style="top:92px;">Corinne@CorinneHalvorsk.com</div>
      <svg class="details__icon" style="top:94px;" width="13" height="10" viewBox="0 0 13 10" aria-hidden="true">
        <rect x="0.5" y="0.5" width="12" height="9" fill="#fff"/>
        <path d="M0.5 0.5 L6.5 5.5 L12.5 0.5" fill="none" stroke="#F6BF27" stroke-width="1.2"/>
      </svg>

      <div class="details__heading">Company Details</div>
      <div class="details__rule details__rule--mid"></div>
      <div class="details__rule details__rule--low"></div>

      <div class="company-row" style="top:192px;">
        <svg width="14" height="14" viewBox="0 0 14 14" aria-hidden="true">
          <rect x="1" y="6" width="7" height="4" rx="2" transform="rotate(-45 4.5 8)" fill="none" stroke="#fff" stroke-width="1.4"/>
          <rect x="6" y="3" width="7" height="4" rx="2" transform="rotate(-45 9.5 5)" fill="none" stroke="#fff" stroke-width="1.4"/>
        </svg>
        <span>www.CorinneHalvorsk.com</span>
      </div>
      <div class="company-row" style="top:216px;">
        <svg width="14" height="14" viewBox="0 0 14 14" aria-hidden="true">
          <circle cx="7" cy="7" r="5" fill="#fff"/>
        </svg>
        <span>@QPZ47</span>
      </div>
      <div class="company-row" style="top:240px;">
        <svg width="14" height="16" viewBox="0 0 14 16" aria-hidden="true">
          <path d="M7 15 C3 10 1.5 8 1.5 5.8 A5.5 5.5 0 0 1 12.5 5.8 C12.5 8 11 10 7 15 Z" fill="#fff"/>
          <circle cx="7" cy="5.8" r="2" fill="#F6BF27"/>
        </svg>
        <span>27 Harbor Lane, Elm Court,<br>New York</span>
      </div>
    </div>
  </section>

</body>
</html>
```